A Clear Three Step Roadmap For Contractors

We are looking for a one-pager "roadmap" that is similar to the 2nd picture we attached, but much more professional & better... please make it landscape orientation. The logo for this system is attached below, as well.

Our Brand Colors to use:
#f2d582
#303030
#8b8c90

The copy we'd like to use on the flyer:
A Clear Three Step Roadmap that will finally allow you to attract quality customers and win more jobs.

The Keystone Ladder Method is a simple to follow system that was created specifically for Contractors and Blue Collar Business Owners.

When it comes to marketing and growing their business, the majority of Contractors are left confused, frustrated and extremely overwhelmed. Unlike most sales, marketing & training programs that offer a single "piece of the puzzle", we've mapped out each essential step of the puzzle and cut out all of the fluff.

All you have to do is complete each step in the right order and we'll be guiding you along the entire journey!

A ---> B

Blueprint: Get clear on where you're going, define your ideal audience, and finally, master your message.
Step 1: Clarify The Chaos
Step 2: Define Your Customer
Step 3: Master Your Message

Build: Attract quality leads, Build your funnel and Formulate a high-converting follow-up system
Step 4: Develop Lead Generator
Step 5: Construct Your Funnel
Step 6: Formulate the Follow-Up

Breakthrough: Get in front of your ideal customers and rapidly scale your business by driving traffic and becoming the authority in your market
Step 7: Turn-On the Traffic
Step 8: Become the Authority
Step 9: Unlock Your Growth

```html
<!DOCTYPE html>
<html lang="en">
<head>
<meta charset="utf-8">
<title>Keystone Ladder Method – One-Page Roadmap</title>
<link href="https://fonts.googleapis.com/css2?family=Lato:wght@300;400;700;900&display=swap" rel="stylesheet">
<style>
  :root{
    --gold:#f2d582;
    --ink:#303030;
    --slate:#8b8c90;
    --mist:#dcdcde;
    --paper:#ffffff;
    --backdrop:#c0bfc0;
  }
  *{margin:0;padding:0;box-sizing:border-box}
  html,body{width:1200px;height:1200px;overflow:hidden;background:var(--backdrop)}
  body{font-family:"Lato",sans-serif;color:var(--ink)}
  .sheet{position:absolute;left:0;top:175px;width:1200px;height:849px;background:var(--paper);overflow:hidden}
  .header{position:absolute;left:0;top:0;width:1200px;height:171px}
  .brand{position:absolute;left:56px;top:50px;display:flex;align-items:center;gap:12px;color:var(--paper);font-weight:700}
  .brand-square{width:56px;height:60px;background:var(--gold)}
  .brand-name{line-height:1}
  .brand-name .top{display:block;font-size:21px;letter-spacing:.3px}
  .brand-name .bottom{display:block;font-size:42px;letter-spacing:2px;margin-top:3px}
  .tagline{position:absolute;left:643px;top:38px;width:512px;font-weight:900;font-size:27.5px;line-height:36px;color:var(--ink)}
  .tagline .mark{position:absolute;font-size:54px;line-height:1;font-family:Georgia,serif;font-weight:900}
  .tagline .open{left:-42px;top:-8px}
  .tagline .close{position:relative;font-size:46px;vertical-align:-14px;margin-left:10px}
  .intro{position:absolute;left:52px;top:210px;width:516px}
  .lead{font-weight:300;font-size:33px;line-height:41px;text-align:justify;text-align-last:left}
  .lead .hl{background:var(--gold);box-shadow:-13px 0 0 var(--gold),4px 0 0 var(--gold)}
  .body-copy{margin-top:28px;font-weight:700;font-size:16.2px;line-height:21px;text-align:justify}
  .body-copy p+p{margin-top:10px}
  .rule{width:89px;height:2px;background:var(--ink);margin-top:25px}
  .promise{margin-top:26px;font-weight:900;font-size:30.5px;line-height:37px}
  .journey{position:absolute;left:184px;top:684px}
  .divider{position:absolute;left:589px;top:196px;height:622px;border-left:2px dashed #b9b9bc}
  .roadmap{position:absolute;left:0;top:0}
  .phase-num{font-weight:900;font-size:52px}
  .phase-title{font-weight:900;font-size:34px}
  .phase-desc{font-weight:400;font-size:16.5px}
  .step-label{font-size:17px;font-weight:400}
  .step-label .strong{font-weight:900}
  .endpoint{font-weight:900;font-size:30px}
</style>
</head>
<body>
<div class="sheet">

  <svg class="header" viewBox="0 0 1200 171" aria-hidden="true">
    <rect x="0" y="0" width="1200" height="150" fill="var(--ink)"/>
    <rect x="0" y="150" width="1200" height="21" fill="var(--slate)"/>
    <polygon points="568,0 1200,0 1200,171 495,171" fill="var(--gold)"/>
  </svg>

  <div class="brand">
    <span class="brand-square"></span>
    <span class="brand-name"><span class="top">KEYSTONE LADDER</span><span class="bottom">METHOD</span></span>
  </div>

  <p class="tagline"><span class="mark open">“</span>A Clear Three Step Roadmap that will finally allow you to attract quality customers and win more jobs.<span class="mark close">”</span></p>

  <section class="intro">
    <p class="lead"><span class="hl">The Keystone Ladder Method</span> is a simple to follow system that was created specifically for Contractors and Blue Collar Business Owners.</p>
    <div class="body-copy">
      <p>When it comes to marketing and growing their business, the majority of Contractors are left confused, frustrated and extremely overwhelmed.</p>
      <p>Unlike most sales, marketing &amp; training programs that offer a single "piece of the puzzle", we've mapped out each essential step of the puzzle and cut out all of the fluff.</p>
    </div>
    <div class="rule"></div>
    <p class="promise">All you have to do is complete each step in the right order and we'll be guiding you along the entire journey!</p>
  </section>

  <svg class="journey" width="250" height="134" viewBox="0 0 250 134" aria-label="From A to B">
    <circle cx="66" cy="66" r="66" fill="var(--gold)"/>
    <circle cx="183" cy="66" r="66" fill="#a8a8ac" style="mix-blend-mode:multiply"/>
    <text x="60" y="84" text-anchor="middle" font-family="Lato,sans-serif" font-weight="900" font-size="50" fill="var(--ink)">A</text>
    <line x1="92" y1="67" x2="150" y2="67" stroke="var(--ink)" stroke-width="4"/>
    <polyline points="140,57 152,67 140,77" fill="none" stroke="var(--ink)" stroke-width="4"/>
    <text x="190" y="84" text-anchor="middle" font-family="Lato,sans-serif" font-weight="900" font-size="50" fill="var(--ink)">B</text>
  </svg>

  <div class="divider"></div>

  <svg class="roadmap" width="1200" height="849" viewBox="0 0 1200 849" font-family="Lato,sans-serif" fill="var(--ink)">
    <rect x="612" y="200" width="550" height="211" fill="var(--gold)"/>
    <rect x="612" y="607" width="550" height="211" fill="var(--mist)"/>

    <g class="phase">
      <text class="phase-num" x="622" y="262" fill="var(--paper)">1</text>
      <text class="phase-title" x="622" y="303">BLUEPRINT</text>
      <text class="phase-desc" x="622" y="328">Get clear on where you're</text>
      <text class="phase-desc" x="622" y="345.5">going, define your ideal</text>
      <text class="phase-desc" x="622" y="363">audience, and finally,</text>
      <text class="phase-desc" x="622" y="380.5">master your message.</text>
    </g>
    <g class="phase">
      <text class="phase-num" x="622" y="474" fill="var(--gold)">2</text>
      <text class="phase-title" x="622" y="514">BUILD</text>
      <text class="phase-desc" x="622" y="537">Attract quality leads, Build</text>
      <text class="phase-desc" x="622" y="554.5">your funnel and Formulate a</text>
      <text class="phase-desc" x="622" y="572">high-converting follow-up</text>
      <text class="phase-desc" x="622" y="589.5">system.</text>
    </g>
    <g class="phase">
      <text class="phase-num" x="622" y="673">3</text>
      <text class="phase-title" x="622" y="715">BREAKTHROUGH</text>
      <text class="phase-desc" x="622" y="738">Get in front of your ideal</text>
      <text class="phase-desc" x="622" y="755.5">customers and rapidly scale</text>
      <text class="phase-desc" x="622" y="773">your business by driving</text>
      <text class="phase-desc" x="622" y="790.5">traffic and becoming the</text>
      <text class="phase-desc" x="622" y="808">authority in your market</text>
    </g>

    <polyline points="887,240 1038,308 887,372 1038,447 887,509 1038,569 887,644 1038,713 887,780" fill="none" stroke="var(--ink)" stroke-width="2.5"/>

    <text class="endpoint" x="820" y="236">A</text>
    <line x1="813" y1="240" x2="852" y2="240" stroke="var(--ink)" stroke-width="2"/>
    <text class="endpoint" x="824" y="801">B</text>
    <line x1="817" y1="805" x2="857" y2="805" stroke="var(--ink)" stroke-width="2"/>

    <g class="step-node" stroke="var(--ink)" stroke-width="3" fill="var(--paper)">
      <circle cx="887" cy="240" r="36"/>
      <circle cx="1038" cy="308" r="36"/>
      <circle cx="887" cy="372" r="36"/>
      <circle cx="1038" cy="447" r="36"/>
      <circle cx="887" cy="509" r="36"/>
      <circle cx="1038" cy="569" r="36"/>
      <circle cx="887" cy="644" r="36"/>
      <circle cx="1038" cy="713" r="36"/>
      <circle cx="887" cy="780" r="36"/>
    </g>
    <g class="step-icon" fill="var(--gold)" opacity="0.85">
      <circle cx="887" cy="240" r="24" role="img" aria-label="Target crosshair icon"/>
      <circle cx="1038" cy="308" r="24" role="img" aria-label="Customer icon"/>
      <circle cx="887" cy="372" r="24" role="img" aria-label="Megaphone icon"/>
      <circle cx="1038" cy="447" r="24" role="img" aria-label="Magnet icon"/>
      <circle cx="887" cy="509" r="24" role="img" aria-label="Funnel icon"/>
      <circle cx="1038" cy="569" r="24" role="img" aria-label="Follow-up list icon"/>
      <circle cx="887" cy="644" r="24" role="img" aria-label="Web traffic icon"/>
      <circle cx="1038" cy="713" r="24" role="img" aria-label="Mountain peak icon"/>
      <circle cx="887" cy="780" r="24" role="img" aria-label="Rocket icon"/>
    </g>

    <g class="step-label">
      <text x="938" y="220"><tspan class="strong">Clarify</tspan></text>
      <text x="938" y="239">The Chaos</text>

      <text x="1083" y="294"><tspan class="strong">Define</tspan></text>
      <text x="1083" y="312">Your</text>
      <text x="1083" y="330">Customer</text>

      <text x="941" y="366"><tspan class="strong">Master</tspan></text>
      <text x="941" y="384">Your Message</text>

      <text x="1083" y="434"><tspan class="strong">Develop</tspan></text>
      <text x="1083" y="452">Lead</text>
      <text x="1083" y="471">Generator</text>

      <text x="941" y="504"><tspan class="strong">Construct</tspan></text>
      <text x="941" y="522">Your Funnel</text>

      <text x="1083" y="551"><tspan class="strong">Formulate</tspan></text>
      <text x="1083" y="569">the</text>
      <text x="1083" y="588">Follow-Up</text>

      <text x="941" y="637"><tspan class="strong">Turn-On</tspan></text>
      <text x="941" y="655">the Traffic</text>

      <text x="1083" y="695"><tspan class="strong">Become</tspan></text>
      <text x="1083" y="713">the</text>
      <text x="1083" y="732">Authority</text>

      <text x="941" y="778"><tspan class="strong">Unlock</tspan></text>
      <text x="941" y="797">Your Growth</text>
    </g>
  </svg>

</div>
</body>
</html>
```